RWM Electrical Business Card Design

Have a logo to use, just looking for design around this, would like green theme, would like symbols in place of phone, fax, email etc.

Business

RWM Electrical, Marcus Thorley, marcus@rwmelectrical.example.au, www.rwmelectrical.example.au, mobile 0491 568 342, phone (07) 3915 4280, fax (07) 3915 4280, facebook and linkedin
addresses

```html
<!DOCTYPE html>
<html lang="en">
<head>
<meta charset="utf-8">
<title>RWM Electrical – Business Card</title>
<link rel="stylesheet" href="https://fonts.googleapis.com/css2?family=Questrial&family=Open+Sans:wght@400;700&display=swap">
<style>
  :root {
    --stage: #1c1c1c;
    --card-dark: #141414;
    --card-light: #f7f7f7;
    --brand-green: #4cb84a;
    --ink: #1a1a1a;
    --ink-soft: #2b2b2b;
    --white: #ffffff;
  }
  * { box-sizing: border-box; margin: 0; padding: 0; }
  html, body {
    width: 1200px;
    height: 900px;
    overflow: hidden;
    background: var(--stage);
  }
  .canvas {
    position: relative;
    width: 1200px;
    height: 900px;
  }
  .card {
    position: absolute;
    left: 280px;
    width: 640px;
    height: 366px;
    box-shadow: 0 10px 30px rgba(0,0,0,0.5);
  }
  .card--back {
    top: 64px;
    background: var(--card-dark);
    display: flex;
    align-items: center;
    justify-content: center;
    gap: 16px;
  }
  .card--front {
    top: 470px;
    background: var(--card-light);
  }
  .brand-dot {
    width: 40px;
    height: 40px;
    border-radius: 50%;
    background: var(--brand-green);
  }
  .brand-name {
    font-family: "Questrial", sans-serif;
    font-size: 46px;
    color: var(--white);
    letter-spacing: 0.5px;
  }
  .front-brand {
    position: absolute;
    left: 58px;
    top: 105px;
    width: 230px;
    display: flex;
    flex-direction: column;
    align-items: center;
    gap: 18px;
  }
  .front-brand .brand-dot {
    width: 120px;
    height: 120px;
  }
  .front-brand .brand-name {
    font-size: 26px;
    color: var(--ink);
  }
  .contact {
    position: absolute;
    left: 350px;
    top: 84px;
    font-family: "Open Sans", sans-serif;
    color: var(--ink-soft);
  }
  .contact-name {
    font-weight: 700;
    font-size: 19px;
    color: var(--ink);
    margin-bottom: 18px;
  }
  .contact-list { list-style: none; }
  .contact-item {
    display: flex;
    align-items: center;
    gap: 18px;
    font-size: 15px;
    line-height: 20px;
    margin-bottom: 12px;
  }
  .contact-icon {
    width: 16px;
    height: 16px;
    flex: none;
    fill: none;
    stroke: var(--brand-green);
    stroke-width: 1.6;
  }
</style>
</head>
<body>
<main class="canvas">
  <section class="card card--back" aria-label="Card back">
    <span class="brand-dot"></span>
    <span class="brand-name">RWM Electrical</span>
  </section>

  <section class="card card--front" aria-label="Card front">
    <div class="front-brand">
      <span class="brand-dot"></span>
      <span class="brand-name">RWM Electrical</span>
    </div>

    <div class="contact">
      <p class="contact-name">Marcus Thorley</p>
      <ul class="contact-list">
        <li class="contact-item">
          <svg class="contact-icon" viewBox="0 0 16 16" aria-label="Mobile"><rect x="4" y="1" width="8" height="14" rx="1.5"/><line x1="7" y1="12.5" x2="9" y2="12.5"/></svg>
          <span>0491 568 342</span>
        </li>
        <li class="contact-item">
          <svg class="contact-icon" viewBox="0 0 16 16" aria-label="Phone"><path d="M2 6c0-2 2.5-3 6-3s6 1 6 3l-2 1-1-2H5L4 7z"/><rect x="3" y="8" width="10" height="6" rx="1"/></svg>
          <span>(07) 3915 4280</span>
        </li>
        <li class="contact-item">
          <svg class="contact-icon" viewBox="0 0 16 16" aria-label="Fax"><rect x="4" y="1.5" width="8" height="4"/><rect x="1.5" y="5.5" width="13" height="6" rx="1"/><rect x="4" y="9.5" width="8" height="5"/></svg>
          <span>(07) 3915 4280</span>
        </li>
        <li class="contact-item">
          <svg class="contact-icon" viewBox="0 0 16 16" aria-label="Email"><rect x="1.5" y="3.5" width="13" height="9"/><polyline points="1.5,3.5 8,9 14.5,3.5"/></svg>
          <span>marcus@rwmelectrical.example.au</span>
        </li>
        <li class="contact-item">
          <svg class="contact-icon" viewBox="0 0 16 16" aria-label="Website"><circle cx="8" cy="8" r="6.5"/><line x1="1.5" y1="8" x2="14.5" y2="8"/><ellipse cx="8" cy="8" rx="3" ry="6.5"/></svg>
          <span>www.rwmelectrical.example.au</span>
        </li>
      </ul>
    </div>
  </section>
</main>
</body>
</html>
```